Business cards, letterhead, envelopes for Business Brokerage Firm
Business cards, letterhead, envelopes, fax cover sheet, postcards
Business cards, letterhead, envelopes for Business Brokerage Firm -
Creative Brief
Professional
Marek Dunholt
President
438 North Ferris Lane, Suite #516 Larkdale, Illinois 60419
marek@kelvrabusinessbrokers.com
www.kelvrabusinessbrokers.com
we do not have a slogan yet, if you have any ideas, feel free to add it in. We like the blues and grays for color.
We Sell Businesses -company sales or mergers -restaurant sales specialist -commercial real estate sales -exit/sale strategy consulting -operations consulting -estimates of value

```html
<!DOCTYPE html>
<html lang="en">
<head>
<meta charset="utf-8">
<title>Kelvra Business Brokers — Stationery Set</title>
<link href="https://fonts.googleapis.com/css2?family=Cormorant+Garamond:wght@500;600&display=swap" rel="stylesheet">
<style>
  :root{
    --navy:#1d3c63;
    --blue:#2f5f8f;
    --teal:#3b7fa6;
    --gray-dark:#6c6e72;
    --gray-mid:#9a9ca0;
    --gray-light:#d9dadc;
    --paper:#ffffff;
    --ink:#2b2b2b;
  }
  *{margin:0;padding:0;box-sizing:border-box}
  html,body{width:1200px;height:746px;overflow:hidden;background:var(--paper)}
  body{position:relative;font-family:"Cormorant Garamond",Georgia,serif;color:var(--ink)}
  .sheet{position:absolute;background:var(--paper);box-shadow:0 0 0 1px #cfd0d2,2px 3px 6px rgba(0,0,0,.18);overflow:hidden}
  .mark{display:flex;align-items:center;gap:8px}
  .mark .dot{border-radius:50%;border:3px solid var(--blue);flex:none}
  .mark .name{color:var(--navy);font-weight:600;font-variant:small-caps;letter-spacing:.04em;line-height:1.05}
  .rule-bar{position:absolute;background:var(--gray-mid)}
  .ghost{position:absolute;border-radius:50%;border:10px solid var(--gray-light);opacity:.7}

  /* letterhead */
  .letterhead{left:24px;top:24px;width:523px;height:696px}
  .letterhead .rule-bar{left:6px;top:0;width:12px;height:696px}
  .letterhead .mark{position:absolute;left:34px;top:16px}
  .letterhead .dot{width:60px;height:60px}
  .letterhead .name{font-size:26px}
  .letterhead .ghost{right:18px;bottom:24px;width:150px;height:150px}
  .lh-footer{position:absolute;left:34px;bottom:26px;font-size:11.5px;line-height:1.45;color:var(--ink)}
  .lh-footer b{color:var(--navy)}

  /* business card front */
  .card-front{left:571px;top:29px;width:257px;height:139px}
  .card-front .mark{position:absolute;left:10px;top:8px;gap:5px}
  .card-front .dot{width:22px;height:22px;border-width:2px}
  .card-front .name{font-size:11px}
  .portrait{position:absolute;left:122px;top:14px;width:34px;height:42px;background:linear-gradient(180deg,#8aa3bd,#3d5470)}
  .person{position:absolute;left:10px;top:78px;font-size:12px;line-height:1.2;text-align:center;width:100px}
  .person small{display:block;font-size:9px;color:var(--gray-dark)}
  .card-contact{position:absolute;left:122px;top:62px;font-size:7px;line-height:1.3;color:var(--ink)}
  .card-front .rule-bar{left:0;bottom:0;width:257px;height:6px}

  /* card backs */
  .card-back{left:845px;top:29px;width:259px;height:139px;background:linear-gradient(135deg,var(--navy),var(--teal));color:#fff}
  .card-alt{left:720px;top:173px;width:259px;height:139px;background:linear-gradient(135deg,var(--gray-dark),#b7b9bc);color:#fff}
  .card-back .mark,.card-alt .mark{position:absolute;left:12px;top:10px;gap:5px}
  .card-back .dot,.card-alt .dot{width:16px;height:16px;border:2px solid #fff}
  .card-back .name,.card-alt .name{color:#fff;font-size:8px}
  .services{position:absolute;left:14px;top:44px;font-size:8.5px;line-height:1.3;list-style:none}
  .services .lead{font-size:13px;margin-bottom:2px}
  .card-back .ghost,.card-alt .ghost{right:16px;top:32px;width:80px;height:80px;border:7px solid rgba(255,255,255,.25)}

  /* envelope */
  .env-flap{position:absolute;left:578px;top:348px;width:596px;height:96px}
  .envelope{left:578px;top:444px;width:596px;height:288px}
  .envelope .rule-bar{left:6px;top:0;width:12px;height:288px}
  .envelope .mark{position:absolute;left:34px;top:22px}
  .envelope .dot{width:56px;height:56px}
  .envelope .name{font-size:24px}
  .env-return{position:absolute;left:34px;top:114px;font-size:11px;line-height:1.35}
  .envelope .ghost{right:26px;bottom:14px;width:120px;height:120px}
</style>
</head>
<body>

<section class="sheet letterhead" aria-label="Letterhead">
  <div class="rule-bar"></div>
  <div class="mark"><span class="dot"></span><span class="name">Kelvra<br>Business<br>Brokers</span></div>
  <div class="ghost"></div>
  <div class="lh-footer">
    438 North Ferris Lane, Suite #516 | Larkdale, Illinois 60419<br>
    <b>Phone:</b> 847.555.0142 | <b>Cell:</b> 847.555.0187 | <b>Fax:</b> 847.555.0193<br>
    <b>Email:</b> marek@kelvrabusinessbrokers.com | www.kelvrabusinessbrokers.com
  </div>
</section>

<section class="sheet card-front" aria-label="Business card front">
  <div class="mark"><span class="dot"></span><span class="name">Kelvra<br>Business<br>Brokers</span></div>
  <div class="portrait" role="img" aria-label="Portrait photo of Marek Dunholt"></div>
  <div class="person">Marek Dunholt<small>President</small></div>
  <div class="card-contact">
    438 North Ferris Lane, Suite #516<br>Larkdale, Illinois 60419<br>
    Office: 847.555.0142<br>Cell: 847.555.0187<br>Fax: 847.555.0193<br>
    marek@kelvrabusinessbrokers.com<br>www.kelvrabusinessbrokers.com
  </div>
  <div class="rule-bar"></div>
</section>

<section class="sheet card-back" aria-label="Business card back, blue">
  <div class="mark"><span class="dot"></span><span class="name">Kelvra<br>Business<br>Brokers</span></div>
  <ul class="services">
    <li class="lead">We Sell Businesses</li>
    <li>Company Sales or Mergers</li>
    <li>Restaurant Sales Specialist</li>
    <li>Commercial Real Estate Sales</li>
    <li>Exit/Sale Strategy Consulting</li>
    <li>Operations Consulting</li>
    <li>Estimates of Value</li>
  </ul>
  <div class="ghost"></div>
</section>

<section class="sheet card-alt" aria-label="Business card back, gray">
  <div class="mark"><span class="dot"></span><span class="name">Kelvra<br>Business<br>Brokers</span></div>
  <ul class="services">
    <li class="lead">We Sell Businesses</li>
    <li>Company Sales or Mergers</li>
    <li>Restaurant Sales Specialist</li>
    <li>Commercial Real Estate Sales</li>
    <li>Exit/Sale Strategy Consulting</li>
    <li>Operations Consulting</li>
    <li>Estimates of Value</li>
  </ul>
  <div class="ghost"></div>
</section>

<svg class="env-flap" viewBox="0 0 596 96" aria-label="Envelope flap">
  <path d="M0 96 V28 Q0 0 40 0 H556 Q596 0 596 28 V96 Z" fill="var(--gray-dark)"/>
  <path d="M0 96 L298 60 L596 96" fill="none" stroke="#5a5c60" stroke-width="1"/>
  <circle cx="298" cy="34" r="16" fill="none" stroke="var(--gray-light)" stroke-width="3"/>
</svg>

<section class="sheet envelope" aria-label="Envelope front">
  <div class="rule-bar"></div>
  <div class="mark"><span class="dot"></span><span class="name">Kelvra<br>Business<br>Brokers</span></div>
  <div class="env-return">438 North Ferris Lane, Suite #516<br>Larkdale, Illinois 60419</div>
  <div class="ghost"></div>
</section>

</body>
</html>
```